New DermaLoom logo and packaging

We would like a new design for our new product DermaLoom, a high strength vitamin C serum which treats pigmentation. The packaging will reflect a high quality, clinical product with the logo "DermaLoom" on the front, with it's ingredients "Vitamin C, B3, B5, E and ferulic acid" the products are in two sizes 10ml and 30ml.

This is one of many products to come out in the DermaLoom range.

It would be for high end medical clinics selling premium brands, with a strong medical and clinical feel, professional and current or even futuristic in appearance.

Gold, blue, silver, White, cream are all colours that do this (without appearing cheap)

The product is not tested on animals, so would have
- "Not tested on animals".
- "12m" symbol for shelf life,
- "Made in USA"
- and ingredients list

See attached the product and existing box

Target Market(s)

Medical and aesthetic clinics

Font styles to use
Serif
Sans Serif

Colors
33a6d7
cee9f5
ffffff
fbed22
fee18a

Requirements
Must have
• High end premium brand
Nice to have
• like the idea of gold and silver lettering on cream background
Should not have
• Tacky, over complicated design

```html
<!DOCTYPE html>
<html lang="en">
<head>
<meta charset="utf-8">
<title>DermaLoom Serum Packaging</title>
<link href="https://fonts.googleapis.com/css2?family=Montserrat:wght@500;600;700&display=swap" rel="stylesheet">
<style>
  :root {
    --brand-blue: #33a6d7;
    --pale-blue: #cee9f5;
    --white: #ffffff;
    --backdrop: #eef0f1;
    --rose-light: #f0cdbb;
    --rose-dark: #c9957e;
  }
  html, body {
    margin: 0;
    padding: 0;
    width: 1200px;
    height: 1200px;
    overflow: hidden;
    background: var(--backdrop);
    font-family: "Montserrat", Arial, sans-serif;
  }
  .canvas {
    position: relative;
    width: 1200px;
    height: 1200px;
  }
  .panel {
    position: absolute;
    display: flex;
    flex-direction: column;
    box-shadow: 0 6px 18px rgba(0,0,0,0.12);
  }
  .panel-top {
    background: var(--white);
    display: flex;
    flex-direction: column;
    align-items: center;
    justify-content: center;
  }
  .rose-band {
    background: linear-gradient(90deg, var(--rose-dark), var(--rose-light) 50%, var(--rose-dark));
  }
  .panel-bottom {
    background: var(--brand-blue);
    color: var(--white);
    flex: 1;
    display: flex;
    flex-direction: column;
    align-items: center;
    text-align: center;
  }
  .brand-name {
    color: var(--brand-blue);
    font-weight: 600;
    letter-spacing: 0.12em;
    margin: 0;
    line-height: 1;
  }
  .brand-by {
    color: var(--brand-blue);
    font-weight: 600;
    letter-spacing: 0.14em;
    text-transform: uppercase;
    margin: 0;
  }
  .product-title {
    font-weight: 600;
    letter-spacing: 0.04em;
    margin: 0;
  }
  .ingredients {
    font-weight: 600;
    letter-spacing: 0.08em;
    text-transform: uppercase;
    margin: 0;
  }
  .volume {
    font-weight: 600;
    letter-spacing: 0.08em;
    margin: 0;
  }

  /* Box front */
  .box-front { left: 416px; top: 192px; width: 370px; height: 766px; }
  .box-front .panel-top { height: 368px; gap: 14px; }
  .box-front .brand-name { font-size: 38px; }
  .box-front .brand-by { font-size: 14px; }
  .box-front .rose-band { height: 14px; }
  .box-front .product-title { font-size: 38px; margin-top: 82px; }
  .box-front .ingredients { font-size: 13px; line-height: 1.65; margin-top: 22px; }
  .box-front .volume { font-size: 13px; margin-top: auto; margin-bottom: 74px; }

  /* Front label */
  .label-front { left: 142px; top: 618px; width: 218px; height: 282px; }
  .label-front .panel-top { height: 137px; gap: 7px; }
  .label-front .brand-name { font-size: 19px; }
  .label-front .brand-by { font-size: 7px; }
  .label-front .rose-band { height: 8px; }
  .label-front .product-title { font-size: 15px; margin-top: 24px; }
  .label-front .ingredients { font-size: 5.5px; line-height: 1.6; margin-top: 8px; }
  .label-front .volume { font-size: 5.5px; margin-top: 22px; }

  /* Back label */
  .label-back { left: 843px; top: 632px; width: 203px; height: 273px; }
  .label-back .panel-top { height: 133px; gap: 6px; }
  .label-back .brand-name { font-size: 17px; }
  .label-back .brand-by { font-size: 6.5px; }
  .label-back .ingredients-list {
    color: var(--brand-blue);
    font-size: 5px;
    font-weight: 600;
    letter-spacing: 0.06em;
    line-height: 1.6;
    text-align: center;
    text-transform: uppercase;
    margin: 22px 0 0;
  }
  .label-back .rose-band { height: 8px; }
  .label-back .claim { font-size: 5px; font-weight: 600; letter-spacing: 0.06em; margin: 22px 0 0; }
  .label-back .icon-row { display: flex; gap: 20px; margin-top: 16px; }
  .label-back .origin { font-size: 5px; font-weight: 600; letter-spacing: 0.06em; margin: 14px 0 0; }
</style>
</head>
<body>
<main class="canvas">

  <section class="panel label-front" aria-label="Front bottle label">
    <div class="panel-top">
      <p class="brand-name">DermaLoom</p>
      <p class="brand-by">by Mednova</p>
    </div>
    <div class="rose-band"></div>
    <div class="panel-bottom">
      <h2 class="product-title">SERUM</h2>
      <p class="ingredients">Vitamin C, B3, B5, E<br>and Ferulic Acid</p>
      <p class="volume">30 ml</p>
    </div>
  </section>

  <section class="panel box-front" aria-label="Outer box front">
    <div class="panel-top">
      <h1 class="brand-name">DermaLoom</h1>
      <p class="brand-by">by Mednova</p>
    </div>
    <div class="rose-band"></div>
    <div class="panel-bottom">
      <h2 class="product-title">SERUM</h2>
      <p class="ingredients">Vitamin C, B3, B5, E<br>and Ferulic Acid</p>
      <p class="volume">30 ml</p>
    </div>
  </section>

  <section class="panel label-back" aria-label="Back bottle label">
    <div class="panel-top">
      <p class="brand-name">DermaLoom</p>
      <p class="brand-by">by Mednova</p>
      <p class="ingredients-list">Ingredients: Vitamin C, B3, B5, E<br>and Ferulic Acid</p>
    </div>
    <div class="rose-band"></div>
    <div class="panel-bottom">
      <p class="claim">NOT TESTED ON ANIMALS</p>
      <div class="icon-row">
        <svg class="icon-recycle" width="22" height="22" viewBox="0 0 22 22" aria-label="Recycle symbol" role="img">
          <circle cx="11" cy="11" r="10" fill="none" stroke="#fff" stroke-width="1.4"/>
          <path d="M6 12 A5 5 0 0 1 14 7" fill="none" stroke="#fff" stroke-width="1.6"/>
          <path d="M12.5 5.2 L15.2 7.2 L12.4 8.8 Z" fill="#fff"/>
          <path d="M16 10 A5 5 0 0 1 8 15" fill="none" stroke="#fff" stroke-width="1.6"/>
          <path d="M9.5 16.8 L6.8 14.8 L9.6 13.2 Z" fill="#fff"/>
        </svg>
        <svg class="icon-shelf-life" width="26" height="24" viewBox="0 0 26 24" aria-label="12 month shelf life symbol" role="img">
          <path d="M4 10 L22 10 L21 22 L5 22 Z" fill="none" stroke="#fff" stroke-width="1.3"/>
          <path d="M3 8 L20 2 L21 5 L4 10.5 Z" fill="none" stroke="#fff" stroke-width="1.3"/>
          <text x="13" y="19" font-family="Montserrat, sans-serif" font-size="6" font-weight="700" fill="#fff" text-anchor="middle">12M</text>
        </svg>
      </div>
      <p class="origin">MADE IN USA</p>
    </div>
  </section>

</main>
</body>
</html>
```